Helix Anchor Works Website

Hello we are a screw piling business based in Sydney.
Screw piling is basically drilling steel into the ground with a excavator.

The website needs to have similar information as http://www.brightgroundworks.com.au/. It is basically the same business.

The business name is Helix Anchor Works.

Logo is attached.

Website needs to be wordpress ready.
With SEO.
Want to be able to edit in wordpress.

Target Market(s)

Business to Business and Normal

Industry/Entity Type

Construction

Coding

Coded - Design and coding required

Number of Pages Required

5+ page

Font styles to use
Serif
Sans Serif
Decorative

Requirements
Nice to have
• Information about screw piering.

```html
<!DOCTYPE html>
<html lang="en">
<head>
<meta charset="utf-8">
<title>Helix Anchor Works</title>
<link rel="stylesheet" href="https://fonts.googleapis.com/css2?family=Open+Sans:wght@400;600;700;800&family=Lato:wght@300;400;700&display=swap">
<style>
:root{
  --blue:#0b5cd5;
  --blue-deep:#0a47a8;
  --navy:#0d3f96;
  --cyan:#5fd0ff;
  --sky:#39a6dc;
  --sky-soft:#9fd3ee;
  --frame:#e5e5e5;
  --ink:#555;
  --dark:#2f2f2f;
  --white:#fff;
}
*{box-sizing:border-box;margin:0;padding:0}
html,body{width:1200px;height:2857px;overflow:hidden}
body{background:var(--frame);font-family:"Open Sans",Arial,sans-serif;color:var(--ink)}
.page{position:relative;width:1200px;height:2857px;overflow:hidden}
.abs{position:absolute}
.sheet{position:absolute;left:15px;top:15px;width:1170px;height:2842px;background:var(--white)}

/* header */
.brand{left:40px;top:44px;display:flex;align-items:center;gap:14px}
.brand-mark{width:44px;height:44px;background:var(--blue)}
.brand-name{font-weight:800;font-size:30px;color:var(--blue);letter-spacing:.5px;text-transform:uppercase;line-height:1}
.call{left:703px;top:35px;font-size:14px;font-weight:600;color:var(--blue)}
.phone-top{left:940px;top:22px;display:flex;align-items:center;gap:10px;font-size:25px;color:var(--blue);font-weight:600}
.nav{right:35px;top:108px;display:flex;gap:21px;font-size:14px;font-weight:700;color:var(--navy)}

/* hero */
.hero{left:15px;top:156px;width:1170px;height:501px;background:linear-gradient(180deg,#b9c3c9 0%,#c9b49a 35%,#b98a5e 70%,#8d6a4c 100%)}
.quote{left:720px;top:213px;width:423px;height:349px;background:rgba(18,28,55,.78);border-radius:3px}
.quote-head{position:absolute;left:-8px;top:0;width:423px;height:52px;background:var(--blue);color:var(--white);font-weight:700;font-size:18px;text-align:center;line-height:52px}
.field{position:absolute;background:var(--blue-deep);color:var(--white);font-size:12px;padding:7px 10px;border-radius:2px}
.quote-btn{position:absolute;left:110px;top:302px;width:203px;height:30px;background:var(--blue);color:var(--white);font-weight:700;font-size:13px;text-align:center;line-height:30px;border-radius:2px}
.dots{left:568px;top:634px;display:flex;gap:8px}
.dots span{width:11px;height:11px;border-radius:50%;background:var(--white)}
.dots span:first-child{background:#7ea6d8}

/* intro */
.intro{left:15px;top:657px;width:1170px;height:200px;background:var(--blue)}
.intro p{position:absolute;left:80px;top:17px;width:1010px;text-align:center;font-family:"Lato",Arial,sans-serif;font-weight:300;font-size:26px;line-height:33px;color:var(--white)}

/* service cards */
.card{position:absolute;top:796px;width:352px;height:408px;box-shadow:0 4px 8px rgba(0,0,0,.18)}
.card-photo{height:187px}
.card-title{position:absolute;left:-12px;top:191px;width:376px;height:42px;background:var(--blue);color:var(--white);font-weight:700;font-size:17px;text-align:center;line-height:42px}
.card-body{position:absolute;top:233px;left:0;width:352px;height:175px;background:linear-gradient(180deg,#fff 0%,#f1f1f1 55%,#d6d6d6 100%);padding:18px 18px;font-size:14px;line-height:21px;color:#666}
.read-more{position:absolute;left:110px;top:122px;width:130px;height:32px;background:var(--blue);color:var(--white);border-radius:3px;font-size:14px;font-weight:600;display:flex;align-items:center;justify-content:center;gap:8px}

/* benefits */
.benefits{left:15px;top:1242px;width:1170px;height:383px;background:var(--blue);color:var(--white)}
.benefits h2{position:absolute;top:30px;width:100%;text-align:center;font-size:27px;font-weight:700}
.benefits .sub{position:absolute;top:78px;width:100%;text-align:center;font-size:15px}
.benefit{position:absolute;width:330px;display:flex;gap:12px}
.benefit-icon{flex:none;width:91px;height:91px;border:2px solid var(--white);border-radius:4px;display:flex;align-items:center;justify-content:center}
.benefit h3{color:var(--cyan);font-size:16.5px;font-weight:600;line-height:20px;margin-bottom:2px}
.benefit p{font-size:13px;line-height:17px}

/* testimonials */
.t-title{left:15px;top:1650px;width:1170px;text-align:center;font-size:27px;font-weight:700;color:var(--blue-deep)}
.t-card{position:absolute;background:linear-gradient(180deg,#fff,#ececec);box-shadow:0 2px 8px rgba(0,0,0,.18)}
.avatar{position:absolute;border-radius:50%;border:5px solid var(--white);box-shadow:0 1px 5px rgba(0,0,0,.25);background:radial-gradient(circle at 50% 40%,#e8d4c3,#b9a796)}
.ribbon{position:absolute;background:var(--sky-soft);color:var(--white);font-size:12px;text-align:center}
.ribbon.main{background:var(--sky);font-size:18px;font-weight:600}
.t-quote{left:726px;top:1742px;width:400px}
.t-quote p{font-size:15.5px;line-height:22px;color:var(--blue);text-indent:52px}
.t-name{left:726px;top:1848px;font-size:18px;font-weight:700;color:var(--blue-deep)}
.btn-blue{background:var(--blue);color:var(--white);font-weight:700;font-size:15px;text-align:center;border-radius:2px}

/* gallery */
.gallery-bar{left:15px;top:2000px;width:1170px;height:77px;background:var(--blue)}
.gallery-bar h2{position:absolute;left:57px;top:22px;font-size:24px;font-weight:700;color:var(--white)}
.filter{position:absolute;top:27px;height:28px;border-radius:14px;background:linear-gradient(180deg,#f6f6f6,#bdbdbd);font-size:11px;font-weight:700;color:#333;display:flex;align-items:center;justify-content:center;gap:10px}
.tile{position:absolute;width:390px;height:260px}

/* footer */
.footer{left:15px;top:2597px;width:1170px;height:209px;background:var(--blue);color:var(--white)}
.footer-name{position:absolute;left:25px;top:68px;font-weight:800;font-size:21px;text-transform:uppercase}
.social{position:absolute;top:129px;width:28px;height:28px;border-radius:50%;background:var(--white)}
.f-line{position:absolute;left:275px;display:flex;gap:12px;font-size:15px;font-weight:600;line-height:18px}
.input{position:absolute;background:var(--white);color:#888;font-size:13px;padding:9px 12px;border-radius:2px}
.send{position:absolute;left:845px;top:124px;width:105px;height:36px;background:#111;color:var(--white);font-weight:700;font-size:14px;text-align:center;line-height:36px}
.copyright{left:15px;top:2806px;width:1170px;height:36px;background:var(--dark);color:#ccc;font-size:11px;text-align:center;line-height:36px}
</style>
</head>
<body>
<div class="page">
  <div class="sheet"></div>

  <!-- header -->
  <div class="abs brand"><span class="brand-mark"></span><span class="brand-name">Helix Anchor Works</span></div>
  <div class="abs call">CALL US FOR FREE ESTIMATE</div>
  <div class="abs phone-top">
    <svg width="40" height="40" viewBox="0 0 40 40"><circle cx="20" cy="20" r="18" fill="none" stroke="#0b5cd5" stroke-width="2.5"/><path d="M14 11l4 0 2 6-3 2c1 3 3 5 6 6l2-3 6 2 0 4c-10 1-18-7-17-17z" fill="#0b5cd5"/></svg>
    <span>02 5550 1847</span>
  </div>
  <nav class="abs nav"><span>ABOUT US</span><span>PRODUCTS</span><span>BENEFITS</span><span>FAQ</span><span>TESTIMONIALS</span><span>GALLERY</span><span>CONTACT US</span></nav>

  <!-- hero -->
  <div class="abs hero" role="img" aria-label="Photo of a piling rig working on a construction site with stacked piles"></div>
  <form class="abs quote">
    <div class="quote-head">REQUEST A FREE QUOTE NOW!</div>
    <div class="field" style="left:25px;top:70px;width:180px">First Name</div>
    <div class="field" style="left:215px;top:70px;width:183px">Last Name</div>
    <div class="field" style="left:25px;top:110px;width:180px">Email Address</div>
    <div class="field" style="left:215px;top:110px;width:183px">Phone Number</div>
    <div class="field" style="left:25px;top:152px;width:373px;height:130px">Detail of Works Required</div>
    <div class="quote-btn">GET A QUOTE</div>
  </form>
  <div class="abs dots"><span></span><span></span><span></span><span></span></div>

  <!-- intro -->
  <section class="abs intro"><p>We have evolved into a unique business in the screw piling industry in that we have our own manufacturing plant producing our piers. We understand the requirements of the fast paced construction industry to ensure our clients receive the best products and services.</p></section>

  <!-- service cards -->
  <article class="card" style="left:40px">
    <div class="card-photo" role="img" aria-label="Photo of a worker beside a screw pile in wet ground" style="background:linear-gradient(180deg,#6f6a63,#4e4a44)"></div>
    <div class="card-title">DOMESTIC</div>
    <div class="card-body">Our domestic range of screw piles ensure your foundations are supplied &amp; installed to the correct depth to meet engineers specifications.
      <div class="read-more">Read More <svg width="16" height="16" viewBox="0 0 16 16"><circle cx="8" cy="8" r="7" fill="none" stroke="#fff" stroke-width="1.6"/><path d="M5 8h6M8 5l3 3-3 3" fill="none" stroke="#fff" stroke-width="1.6"/></svg></div>
    </div>
  </article>
  <article class="card" style="left:424px">
    <div class="card-photo" role="img" aria-label="Photo of steel reinforcement mesh on a commercial site" style="background:linear-gradient(180deg,#8a8580,#5f5a55)"></div>
    <div class="card-title">COMMERCIAL</div>
    <div class="card-body">Our commercial screw piles cover a large range of loads to accommodate the needs of clients in the commercial building sector.
      <div class="read-more">Read More <svg width="16" height="16" viewBox="0 0 16 16"><circle cx="8" cy="8" r="7" fill="none" stroke="#fff" stroke-width="1.6"/><path d="M5 8h6M8 5l3 3-3 3" fill="none" stroke="#fff" stroke-width="1.6"/></svg></div>
    </div>
  </article>
  <article class="card" style="left:810px">
    <div class="card-photo" role="img" aria-label="Photo of a row of pile caps beside water" style="background:linear-gradient(180deg,#b7c7c9,#8fa2a8)"></div>
    <div class="card-title">DEMOUNTABLE</div>
    <div class="card-body">Ideal screw piles are efficiently used as raised piers to support mining camps, solar panels, granny flats as well as timber or steel bearer and joist sub-floors.
      <div class="read-more">Read More <svg width="16" height="16" viewBox="0 0 16 16"><circle cx="8" cy="8" r="7" fill="none" stroke="#fff" stroke-width="1.6"/><path d="M5 8h6M8 5l3 3-3 3" fill="none" stroke="#fff" stroke-width="1.6"/></svg></div>
    </div>
  </article>

  <!-- benefits -->
  <section class="abs benefits">
    <h2>BENEFITS OF SCREW PILES</h2>
    <p class="sub">Ideal screw piles when compared with concrete bored piers have a number of advantages:</p>

    <div class="benefit" style="left:84px;top:120px">
      <div class="benefit-icon"><svg width="56" height="56" viewBox="0 0 56 56" fill="none" stroke="#fff" stroke-width="3"><circle cx="28" cy="28" r="22"/><path d="M15 34a14 14 0 1 1 26 0"/><path d="M28 28l8-9"/><circle cx="28" cy="28" r="3" fill="#fff"/></svg></div>
      <div><h3>Speed of Installation</h3><p>Lorem ipsum dolor sit amet, consec tetuer adipiscing elit, sed diam no nummy nibh euismod tincidunt ut laoreet dolore magna.</p></div>
    </div>
    <div class="benefit" style="left:431px;top:120px">
      <div class="benefit-icon"><svg width="56" height="56" viewBox="0 0 56 56" fill="none" stroke="#fff" stroke-width="3.5"><rect x="8" y="10" width="38" height="38" rx="2"/><path d="M17 28l9 9 22-26"/></svg></div>
      <div><h3>No Spoil Removal</h3><p>Lorem ipsum dolor sit amet, consec tetuer adipiscing elit, sed diam no nummy nibh euismod.</p></div>
    </div>
    <div class="benefit" style="left:779px;top:120px">
      <div class="benefit-icon"><svg width="56" height="56" viewBox="0 0 56 56"><text x="28" y="46" text-anchor="middle" font-family="Open Sans, sans-serif" font-size="48" font-weight="700" fill="#fff">$</text></svg></div>
      <div><h3>Cost Effective</h3><p>Lorem ipsum dolor sit amet, consec tetuer adipiscing elit, sed diam no nummy nibh euismod.</p></div>
    </div>
    <div class="benefit" style="left:84px;top:255px">
      <div class="benefit-icon"><svg width="56" height="56" viewBox="0 0 56 56" fill="#fff"><path d="M22 44c-8-2-13-10-10-18 6 0 13 6 10 18z"/><path d="M26 40c0-14 8-22 20-24 1 12-6 22-20 24z"/><path d="M10 48h36" stroke="#fff" stroke-width="3"/></svg></div>
      <div><h3>Environmental Friendly</h3><p>Lorem ipsum dolor sit amet, consec tetuer adipiscing elit, sed diam no nummy nibh euismod tincidunt ut laoreet dolore magna.</p></div>
    </div>
    <div class="benefit" style="left:431px;top:255px">
      <div class="benefit-icon"><svg width="56" height="56" viewBox="0 0 56 56" fill="none" stroke="#fff" stroke-width="3.5"><path d="M28 6l18 7v13c0 12-8 20-18 24C18 46 10 38 10 26V13z"/><path d="M19 28l7 7 12-13"/></svg></div>
      <div><h3>Suitable for All Soil Types</h3><p>Lorem ipsum dolor sit amet, consec tetuer adipiscing elit, sed diam no nummy nibh euismod tincidunt ut laoreet dolore magna.</p></div>
    </div>
    <div class="benefit" style="left:779px;top:255px">
      <div class="benefit-icon"><svg width="60" height="56" viewBox="0 0 60 56" fill="none" stroke="#fff" stroke-width="3"><rect x="8" y="12" width="44" height="22" rx="2"/><circle cx="30" cy="23" r="6"/><path d="M8 40h44M8 46h44"/></svg></div>
      <div><h3>Control Foundation Costs</h3><p>Lorem ipsum dolor sit amet, consec tetuer adipiscing elit, sed diam no nummy nibh euismod tincidunt ut laoreet dolore magna.</p></div>
    </div>
  </section>

  <!-- testimonials -->
  <h2 class="abs t-title">TESTIMONIALS</h2>
  <div class="t-card" style="left:88px;top:1735px;width:172px;height:200px"></div>
  <div class="t-card" style="left:474px;top:1735px;width:170px;height:200px"></div>
  <div class="ribbon" style="left:82px;top:1893px;width:570px;height:30px;line-height:30px">
    <span style="position:absolute;left:38px">Nora Field</span><span style="position:absolute;right:40px">Owen Hale</span>
  </div>
  <div class="t-card" style="left:257px;top:1712px;width:219px;height:258px"></div>
  <div class="ribbon main" style="left:245px;top:1905px;width:243px;height:44px;line-height:44px">Marcus Dell</div>
  <div class="avatar" role="img" aria-label="Portrait of client Nora Field" style="left:130px;top:1772px;width:96px;height:96px"></div>
  <div class="avatar" role="img" aria-label="Portrait of client Marcus Dell" style="left:306px;top:1748px;width:120px;height:120px"></div>
  <div class="avatar" role="img" aria-label="Portrait of client Owen Hale" style="left:500px;top:1772px;width:96px;height:96px"></div>

  <svg class="abs" style="left:724px;top:1740px" width="44" height="32" viewBox="0 0 44 32" fill="#0a47a8"><path d="M0 0h18v18l-8 14H3l6-14H0zM24 0h18v18l-8 14h-7l6-14h-9z"/></svg>
  <div class="abs t-quote"><p>Lorem ipsum dolor sit amet, consectetuer mod tincidunt ut laoreet dolore magna iam, quis nostrud exerci tation ul lamcorper do consequat.</p></div>
  <svg class="abs" style="left:1025px;top:1808px" width="44" height="32" viewBox="0 0 44 32" fill="#0a47a8"><path d="M44 32H26V14l8-14h7l-6 14h9zM20 32H2V14l8-14h7l-6 14h9z"/></svg>
  <div class="abs t-name">Marcus Dell</div>
  <div class="abs btn-blue" style="left:724px;top:1907px;width:300px;height:40px;line-height:40px">VIEW ALL TESTIMONIALS</div>

  <!-- gallery -->
  <section class="abs gallery-bar">
    <h2>PROJECT GALLERY</h2>
    <div class="filter" style="left:602px;width:157px"><svg width="18" height="16" viewBox="0 0 18 16"><path d="M2 8l5 5L16 2" fill="none" stroke="#0b5cd5" stroke-width="3"/></svg>ALL PROJECTS</div>
    <div class="filter" style="left:775px;width:150px"><svg width="14" height="16" viewBox="0 0 14 16"><rect x="1" y="1" width="12" height="14" fill="#333"/></svg>FINISHED</div>
    <div class="filter" style="left:942px;width:155px"><svg width="14" height="16" viewBox="0 0 14 16"><rect x="1" y="1" width="12" height="14" fill="none" stroke="#333" stroke-width="2"/></svg>IN PROGRESS</div>
  </section>
  <div class="tile" role="img" aria-label="Photo of concrete piles standing on a site" style="left:15px;top:2077px;background:linear-gradient(180deg,#6fa6d9 0%,#a8c8e4 50%,#b68f62 70%,#8a6a4a 100%)"></div>
  <div class="tile" role="img" aria-label="Photo of a worker beside a pile in wet ground" style="left:405px;top:2077px;background:linear-gradient(180deg,#6e6a63,#4b4741)"></div>
  <div class="tile" role="img" aria-label="Photo of pile caps in a row beside water" style="left:795px;top:2077px;width:390px;background:linear-gradient(180deg,#9ab48f 0%,#b8c9cc 40%,#8ea3ab 100%)"></div>
  <div class="tile" role="img" aria-label="Photo of stacked piles and machinery on site" style="left:15px;top:2337px;background:linear-gradient(180deg,#8aa7bf 0%,#b29a7b 45%,#8e7358 100%)"></div>
  <div class="tile" role="img" aria-label="Photo of a worker tying steel mesh" style="left:405px;top:2337px;background:linear-gradient(180deg,#837e78,#5a5550)"></div>
  <div class="tile" role="img" aria-label="Photo of concrete piles under a blue sky" style="left:795px;top:2337px;background:linear-gradient(180deg,#3f84d1 0%,#8ab6e0 55%,#b79a73 80%,#9a7b58 100%)"></div>

  <!-- footer -->
  <footer class="abs footer">
    <div class="footer-name">Helix Anchor Works</div>
    <span class="social" style="left:76px"></span><span class="social" style="left:108px"></span><span class="social" style="left:140px"></span>
    <div class="f-line" style="top:40px">
      <svg width="14" height="20" viewBox="0 0 14 20"><path d="M7 0a7 7 0 0 1 7 7c0 5-7 13-7 13S0 12 0 7a7 7 0 0 1 7-7z" fill="#fff"/><circle cx="7" cy="7" r="2.5" fill="#0b5cd5"/></svg>
      <span>Lorem Ipsum Drive<br>Harbour Row, Eastfield<br>NSW 2000<br>Sydney</span>
    </div>
    <div class="f-line" style="top:122px">
      <svg width="16" height="16" viewBox="0 0 16 16"><path d="M2 1h4l1 4-2 1c1 2 3 4 5 5l1-2 4 1v4C7 15 1 9 2 1z" fill="#fff"/></svg>
      <span>02 5550 1847</span>
    </div>
    <div class="f-line" style="top:162px">
      <svg width="18" height="14" viewBox="0 0 18 14"><rect x="0" y="0" width="18" height="14" fill="#fff"/><path d="M0 0l9 8 9-8" fill="none" stroke="#0b5cd5" stroke-width="1.5"/></svg>
      <span>info@helixanchor.com.au</span>
    </div>
    <div class="input" style="left:535px;top:30px;width:300px;height:36px">Name</div>
    <div class="input" style="left:535px;top:77px;width:300px;height:36px">Email</div>
    <div class="input" style="left:535px;top:124px;width:300px;height:36px">Phone</div>
    <div class="input" style="left:845px;top:30px;width:300px;height:83px">Message</div>
    <div class="send">SEND</div>
  </footer>
  <div class="abs copyright">© 2015 HELIX ANCHOR WORKS. ALL RIGHTS RESERVED.</div>
</div>
</body>
</html>
```